Professional digital stationary

We need a digital stationary for our brand, we already have a logo and based on that we need a design for Word, Powerpoint, mailings and Linkedin. We need to be able to re use the stationary for other things like other social media. So basically what we ask is a template for Powerpoint and Word, some e-mail headers and a nice and professional Linkedin Header.

Target Market(s)

recruitment

Font styles to use
Sans Serif

```html
<!DOCTYPE html>
<html lang="en">
<head>
<meta charset="utf-8">
<title>Stridewell Digital Stationery</title>
<link href="https://fonts.googleapis.com/css2?family=Questrial&family=Arimo:wght@400;700&family=Roboto+Condensed:wght@400;700&display=swap" rel="stylesheet">
<style>
:root{
  --green:#acce5c;
  --ink:#444345;
  --text:#3a3a3a;
  --muted:#777;
  --photo:#4a4647;
  --paper:#fbfbfb;
  --board:#dddddd;
  --logo-font:'Questrial',sans-serif;
  --body-font:'Arimo',sans-serif;
  --head-font:'Roboto Condensed',sans-serif;
}
*{box-sizing:border-box;margin:0;padding:0}
html,body{width:1200px;height:757px;overflow:hidden;background:var(--board)}
.board{position:relative;width:1200px;height:757px;font-family:var(--body-font);color:var(--text)}
.page{position:absolute;background:var(--paper);box-shadow:2px 3px 5px rgba(0,0,0,.28);overflow:hidden}
.abs{position:absolute}
.footer-rule{position:absolute;left:0;right:0;bottom:0;height:8px;border-top:2px solid var(--ink);background:var(--green);background-clip:content-box;padding-top:2px}

/* letterhead */
.letter{left:76px;top:61px;width:449px;height:631px;background:linear-gradient(160deg,#fff 30%,#eeeeee)}
.letter .brand{left:33px;top:37px;font-family:var(--logo-font);font-size:32px;color:var(--green);letter-spacing:.5px;line-height:1}
.letter .tagline{left:34px;top:68px;font-family:var(--logo-font);font-size:7.5px;color:var(--text)}
.vdivider{position:absolute;top:43px;height:33px;width:1px;background:#999}
.letter .company{left:218px;top:48px;font-family:var(--logo-font);font-size:6.5px;line-height:8.2px;color:var(--muted)}
.letter .company b{font-weight:400;color:var(--green)}
.contact{left:343px;top:50px;font-family:var(--logo-font);font-size:6.5px;line-height:8.2px;color:var(--muted)}
.contact li{list-style:none;display:flex;align-items:center;gap:6px}
.contact svg{width:5px;height:5px;fill:var(--green)}
.salutation{left:34px;top:157px;font-size:10.5px;color:var(--ink)}
.letter-body{left:34px;top:190px;width:382px;font-size:6.3px;line-height:9.6px;text-align:justify;color:#555}
.letter-body p{margin-bottom:9.6px}
.closing{left:34px;top:401px;font-size:6.5px;color:#555}
.signature{left:30px;top:420px;width:135px;height:42px;background:linear-gradient(90deg,#e6e6e6,#f4f4f4);border-radius:3px}

/* slides */
.slide{width:263px;height:198px}
.s1{left:564px;top:61px}.s2{left:847px;top:61px}
.s3{left:564px;top:275px}.s4{left:847px;top:275px}
.s5{left:564px;top:493px}.s6{left:847px;top:493px;background:var(--green)}
.heading{left:14px;top:11px;font-family:var(--head-font);font-weight:700;font-size:11.5px;color:var(--green)}
.subheading{left:14px;top:25px;font-family:var(--head-font);font-weight:700;font-size:6px;color:var(--ink)}
.head-rule{position:absolute;left:57px;right:15px;top:31px;height:1px;background:#999}
.mini-brand{right:15px;top:17px;font-family:var(--logo-font);font-size:10px;color:var(--green)}
.tiny{font-size:3.7px;line-height:5.6px;color:#444;text-align:justify}
.group-title{font-family:var(--head-font);font-weight:700;font-size:6px;color:var(--green);margin-bottom:3px}

.s1 .brand{left:0;right:0;top:36px;text-align:center;font-family:var(--logo-font);font-size:36px;color:var(--green);line-height:1}
.s1 .tagline{left:52px;top:72px;font-family:var(--logo-font);font-size:8px;color:var(--text)}
.welcome{left:0;right:0;top:125px;bottom:0;border-top:2px solid var(--ink);background:var(--green);color:#fff;text-align:center;font-family:var(--head-font);padding-top:9px;line-height:17px}
.welcome .l1{font-size:13px}.welcome .l2{font-size:15.5px;font-weight:700}.welcome .l3{font-size:12.5px}

.photo{position:absolute;top:56px;width:52px;height:52px;background:var(--photo);border:1.5px solid #fff;box-shadow:0 0 2px rgba(0,0,0,.45);color:#ddd;font-size:6.5px;display:flex;align-items:center;justify-content:center}
.member{position:absolute;top:121px;width:50px}
.member .name{font-size:5.2px;color:var(--green)}
.member .role{font-size:5px;font-style:italic;color:#666;margin:3px 0 6px}

.col{position:absolute;width:114px}
.thanks{left:0;right:0;top:60px;text-align:center;color:#fff;font-family:var(--logo-font)}
.thanks .big{font-size:37px;line-height:1}
.thanks .small{font-size:20px;line-height:1;margin-top:2px}
.address{left:0;right:0;top:169px;text-align:center;color:#fff;font-size:4.6px;line-height:6.4px}
</style>
</head>
<body>
<main class="board">

  <!-- Letterhead -->
  <section class="page letter">
    <div class="abs brand">stridewell</div>
    <div class="abs tagline">More reach, more choice</div>
    <span class="vdivider" style="left:196px"></span>
    <div class="abs company"><b>StridewellLLC</b><br>4120 Juniper Court<br>Boulder, Colorado 80302</div>
    <span class="vdivider" style="left:322px"></span>
    <ul class="abs contact">
      <li><svg viewBox="0 0 10 10"><path d="M2 0l2 2-1 2a6 6 0 003 3l2-1 2 2-2 2C4 10 0 6 0 2z"/></svg>555-014-2290</li>
      <li><svg viewBox="0 0 10 10"><path d="M0 2h10v6H0zM0 2l5 4 5-4" stroke="#fff" stroke-width=".8"/></svg>info@stridewell.com</li>
      <li><svg viewBox="0 0 10 10"><circle cx="5" cy="5" r="5"/></svg>www.stridewell.com</li>
    </ul>
    <div class="abs salutation">Dear Mr. Harlow,</div>
    <div class="abs letter-body">
      <p>Lorem ipsum dolor sit amet, consectetur adipiscing elit. Donec orci purus, luctus vitae dignissim eu, iaculis sed purus. Vivamus faucibus, ipsum nec aliquet viverra, leo mauris condimentum ligula, sit amet sagittis enim ligula quis arcu. Nam egestas tortor id nisi porttitor mattis. In tortor ante, ultricies in suscipit a, tempus non massa. Vivamus et auctor mi. Fusce vel massa nulla. Phasellus nec eros mauris, et scelerisque orci.</p>
      <p>Donec malesuada orci vitae nulla accumsan porta a id massa. Quisque accumsan iaculis magna sit amet fringilla. Maecenas consequat, magna eget tincidunt semper, odio nibh rutrum mi, id feugiat ante nisi eu risus. Vestibulum nunc orci, rhoncus a placerat in, ultricies in mi. Cras mattis varius eros, vel fringilla nisi suscipit eget. Quisque scelerisque sagittis nulla at porttitor.</p>
      <p>Sed id augue vitae urna euismod commodo aliquet a quam. Pellentesque arcu velit, cursus et malesuada ut, consequat et diam. Nullam erat sem, rhoncus id ullamcorper vitae, rhoncus et arcu. In ultricies ultricies nulla, ut rutrum nisi iaculis at. Donec eu magna a metus ornare faucibus. Fusce aliquet faucibus ultricies. Morbi semper, est id tincidunt gravida, sem arcu adipiscing lacus, ac bibendum nulla leo eu purus. Quisque nec diam sed risus consectetur a cumsan quis quis nibh. Vestibulum id purus lorem.</p>
      <p>It is a long established fact that a reader will be distracted by the readable content of a page when looking at its layout. The point of using Lorem Ipsum is that it has a more-or-less normal distribution of letters, as opposed to using 'Content here, content here', making it look like readable English. Many desktop publishing packages</p>
      <p>ada ut, consequat et diam. Nullam erat sem, rhoncus id ullamcorper vitae, rhoncus et arcu. In ultricies ultricies nulla, ut rutrum nisi iaculis at. Donec eu magna a metus ornare faucibus. Fusce aliquet faucibus ultricies. Morbi semper,</p>
    </div>
    <div class="abs closing">Sincerely,</div>
    <div class="abs signature" role="img" aria-label="Handwritten signature of the sender"></div>
    <div class="footer-rule"></div>
  </section>

  <!-- Title slide -->
  <section class="page slide s1">
    <div class="abs brand">stridewell</div>
    <div class="abs tagline">More reach, more choice</div>
    <div class="abs welcome">
      <div class="l1">Welcome to Our</div>
      <div class="l2">Presentation Name</div>
      <div class="l3">Description</div>
    </div>
  </section>

  <!-- Team slide -->
  <section class="page slide s2">
    <div class="abs heading">Heading Here</div>
    <div class="abs subheading">Sub Heading</div>
    <span class="head-rule"></span>
    <div class="abs mini-brand">stridewell</div>
    <div class="photo" style="left:19px" role="img" aria-label="Team member portrait">Photo</div>
    <div class="photo" style="left:78px" role="img" aria-label="Team member portrait">Photo</div>
    <div class="photo" style="left:136px" role="img" aria-label="Team member portrait">Photo</div>
    <div class="photo" style="left:194px" role="img" aria-label="Team member portrait">Photo</div>
    <div class="member" style="left:21px"><div class="name">Team member1</div><div class="role">Title</div><div class="tiny">Lorem ipsum dolor sit amet, consectetur adipiscing elit, sed do eiusmod tempor incididunt</div></div>
    <div class="member" style="left:79px"><div class="name">Team member2</div><div class="role">Title</div><div class="tiny">ut labore et dolore magna aliqua. Ut enim ad minim veniam, quis nostrud exercitation</div></div>
    <div class="member" style="left:137px"><div class="name">Team member3</div><div class="role">Title</div><div class="tiny">ullamco laboris nisi ut aliquip ex ea commodo consequat. Enim ad minim veniam,</div></div>
    <div class="member" style="left:194px"><div class="name">Team member4</div><div class="role">Title</div><div class="tiny">Do eiusmod tempor incididunt. Lorem ipsum dolor sit amet, consectetur adipiscing elit, sed</div></div>
    <div class="footer-rule"></div>
  </section>

  <!-- Groups slide -->
  <section class="page slide s3">
    <div class="abs heading">Heading Here</div>
    <div class="abs subheading">Sub Heading</div>
    <span class="head-rule"></span>
    <div class="abs mini-brand">stridewell</div>
    <div class="col" style="left:16px;top:48px"><div class="group-title">Group1</div><div class="tiny">Lorem ipsum dolor sit amet, consectetur adipiscing elit, sed do eiusmod tempor incididunt ut labore et dolore magna aliqua. Ut enim ad minim veniam, quis nostrud exercitation ullamco laboris nisi ut aliquip ex ea commodo consequat.</div></div>
    <div class="col" style="left:135px;top:48px"><div class="group-title">Group4</div><div class="tiny">Lorem ipsum dolor sit amet, consectetur adipiscing elit, sed do eiusmod tempor incididunt ut labore et dolore magna aliqua. Ut enim ad minim veniam, quis nostrud exercitation ullamco laboris nisi ut aliquip ex ea commodo consequat.</div></div>
    <div class="col" style="left:16px;top:93px"><div class="group-title">Group2</div><div class="tiny">Duis aute irure dolor in reprehenderit in voluptate velit esse cillum dolore eu fugiat nulla pariatur. Excepteur sint occaecat cupidatat non proident, sunt in culpa qui officia deserunt mollit anim id est laborum.</div></div>
    <div class="col" style="left:135px;top:93px"><div class="group-title">Group5</div><div class="tiny">Duis aute irure dolor in reprehenderit in voluptate velit esse cillum dolore eu fugiat nulla pariatur. Excepteur sint occaecat cupidatat non proident, sunt in culpa qui officia deserunt mollit anim id est laborum.</div></div>
    <div class="col" style="left:16px;top:134px"><div class="group-title">Group3</div><div class="tiny">Duis aute irure dolor in reprehenderit in voluptate velit esse cillum dolore eu fugiat nulla pariatur. Excepteur sint occaecat cupidatat non proident, sunt in culpa qui officia deserunt mollit anim id est laborum.</div></div>
    <div class="col" style="left:135px;top:134px"><div class="group-title">Group6</div><div class="tiny">Duis aute irure dolor in reprehenderit in voluptate velit esse cillum dolore eu fugiat nulla pariatur. Excepteur sint occaecat cupidatat non proident, sunt in culpa qui officia deserunt mollit anim id est laborum.</div></div>
    <div class="footer-rule"></div>
  </section>

  <!-- Bar chart slide -->
  <section class="page slide s4">
    <div class="abs heading">Heading Here</div>
    <div class="abs subheading">Sub Heading</div>
    <span class="head-rule"></span>
    <div class="abs mini-brand">stridewell</div>
    <svg class="abs" style="left:24px;top:48px" width="106" height="82" viewBox="0 0 106 82">
      <g stroke="#d4d4d4" stroke-width=".5">
        <line x1="0" y1="1" x2="106" y2="1"/><line x1="0" y1="9" x2="106" y2="9"/><line x1="0" y1="17" x2="106" y2="17"/>
        <line x1="0" y1="25" x2="106" y2="25"/><line x1="0" y1="33" x2="106" y2="33"/><line x1="0" y1="41" x2="106" y2="41"/>
        <line x1="0" y1="49" x2="106" y2="49"/><line x1="0" y1="57" x2="106" y2="57"/><line x1="0" y1="65" x2="106" y2="65"/>
        <line x1="0" y1="73" x2="106" y2="73"/><line x1="0" y1="81" x2="106" y2="81"/>
      </g>
      <g fill="var(--green)">
        <rect x="25" y="4" width="12" height="77"/><rect x="41" y="15" width="12" height="66"/>
        <rect x="57" y="34" width="12" height="47"/><rect x="73" y="20" width="12" height="61"/>
      </g>
      <g fill="#fff" font-size="4" font-family="Arimo, sans-serif">
        <text transform="translate(33 78) rotate(-90)">Sub text1</text><text transform="translate(49 78) rotate(-90)">Sub text2</text>
        <text transform="translate(65 78) rotate(-90)">Sub text3</text><text transform="translate(81 78) rotate(-90)">Sub text4</text>
      </g>
    </svg>
    <div class="abs tiny" style="left:159px;top:49px;width:80px;text-align:left">Lorem ipsum dolor sit amet,<br>consectetur adipiscing elit, sed do<br>eiusmod tempor incididunt ut labore<br>et dolore magna aliqua.<br>Ut enim ad minim veniam,<br>quis nostrud.</div>
    <div class="abs tiny" style="left:159px;top:89px;width:80px;text-align:left">consectetur adipiscing elit, sed do<br>eiusmod tempor incididunt ut labore<br>Lorem ipsum dolor sit amet,<br>et dolore magna aliqua.<br>Ut enim ad minim veniam,<br>quis nostrud.</div>
    <div class="abs tiny" style="left:21px;top:145px;width:220px">Lorem ipsum dolor sit amet, consectetur adipiscing elit, sed do eiusmod tempor incididunt ut labore et dolore magna aliqua. Ut enim ad minim veniam, quis nostrud exercitation ullamco laboris nisi ut aliquip ex ea commodo consequat. Duis aute irure dolor in reprehenderit in voluptate velit esse cillum dolore eu fugiat nulla pariatur. Excepteur sint occaecat cupidatat non proident, sunt in culpa qui officia deserunt mollit anim id est laborum.</div>
    <div class="footer-rule"></div>
  </section>

  <!-- Pie chart slide -->
  <section class="page slide s5">
    <div class="abs heading">Heading Here</div>
    <div class="abs subheading">Sub Heading</div>
    <span class="head-rule"></span>
    <div class="abs mini-brand">stridewell</div>
    <div class="abs tiny" style="left:18px;top:63px;width:111px;text-align:center">Lorem ipsum dolor sit amet, consectetur adipiscing elit, sed do eiusmod tempor incididunt ut labore et dolore magna aliqua. Ut enim ad minim veniam, quis nostrud exercitation ullamco laboris nisi ut aliquip ex ea commodo consequat. Duis aute irure dolor in reprehenderit in voluptate velit esse cillum dolore eu fugiat nulla pariatur. Excepteur sint occaecat cupidatat non proident, sunt in culpa qui officia deserunt mollit anim id est laborum. Ut enim ad minim veniam, quis nostrud exercitation ullamco laboris nisi ut aliquip ex ea commodo consequat.</div>
    <div class="abs tiny" style="left:18px;top:138px;width:111px;text-align:center">Excepteur sint occaecat cupidatat non proident, sunt in culpa qui officia deserunt mollit anim id est laborum. Ut enim ad minim veniam, quis nostrud exercitation ullamco laboris nisi ut aliquip ex ea commodo consequat.</div>
    <svg class="abs" style="left:163px;top:55px" width="60" height="60" viewBox="-30 -30 60 60">
      <g stroke="#fff" stroke-width=".8">
        <path d="M0 0L-7.5-28A29 29 0 0 1 22.2-18.6Z" fill="var(--ink)"/>
        <path d="M0 0L22.2-18.6A29 29 0 0 1 28.9 2.5Z" fill="var(--green)"/>
        <path d="M0 0L28.9 2.5A29 29 0 0 1 9.9 27.3Z" fill="var(--ink)"/>
        <path d="M0 0L9.9 27.3A29 29 0 1 1 -7.5-28Z" fill="var(--green)"/>
      </g>
    </svg>
    <svg class="abs" style="left:162px;top:124px" width="76" height="18" viewBox="0 0 76 18">
      <rect x="0" y="1" width="4" height="4" fill="var(--green)"/>
      <text x="8" y="4.6" font-size="3.8" font-family="Arimo, sans-serif" fill="#444">Lorem ipsum dolor sit amet 50%</text>
      <line x1="0" y1="7.5" x2="76" y2="7.5" stroke="#777" stroke-width=".4"/>
      <rect x="0" y="10" width="4" height="4" fill="var(--ink)"/>
      <text x="8" y="13.6" font-size="3.8" font-family="Arimo, sans-serif" fill="#444">Duis aute irure dolor in 50%</text>
      <line x1="0" y1="16.5" x2="76" y2="16.5" stroke="#777" stroke-width=".4"/>
    </svg>
    <div class="abs tiny" style="left:162px;top:147px;width:80px;text-align:left">sunt in culpa qui officia deserunt mollit anim id est laborum. Ut enim ad minim veniam</div>
    <div class="footer-rule"></div>
  </section>

  <!-- Closing slide -->
  <section class="page slide s6">
    <div class="abs thanks">
      <div class="big">Thanks</div>
      <div class="small">For Coming</div>
    </div>
    <div class="abs address">4120 Juniper Court, Boulder, Colorado 80302<br>P : 555-014-2290 M : 555-014-7731 E : info@stridewell.com W : www.stridewell.com</div>
  </section>

</main>
</body>
</html>
```